Wordpress Design Project

WHO WE ARE:
Bright Path Web Growth is not just another SEO or PPC company. We work with our clients to help them grow their business and achieve their goals. Our commitment to doing what is best for the customer, is why we have grown so quickly. We believe our business is not about advertising BUT about connecting customers & growing our clients businesses. We see our product as helping people, not selling a product.

PROJECT OVERVIEW:
I need to create a wordpress website for my business, www.brightpathwebgrowth.com.au

I need a whole new site created showing all of my services. The services include:
NOTE: These are not the main focus of the home page.

Consulting & Strategy Planning
Search Engine Optimisation
Pay Per Click
Re-Marketing

Once I have selected the top home page design, I will need a product and blog page designed.

SITE DESIGN:
If I was to explain the kind of style I am looking for, it would be high-street, New York agency look, web 2.0. Clean, elegant, stylish, high quality and simple looking. Kind of like you would expect from an quince website.

Think of car advertising, the closest to the target market & look/feel Im looking for would be Ravenmotor, Korel, Tamar, Brandin, Zepra.

However, I am open to any design style.

DO NOT let this restrict your creativity BUT here are some websites I like the look of.

Home page:
http://www.layoutfoundry.example/demo/52816.html
https://www.vantorix.example/intl/en/halo/devices/
http://www.vantorix.example/intl/en/halo/devices/features-different.html
http://www.layoutfoundry.example/demo/47190.html
https://www.vantorix.example/intl/en/halo/browser/features.html

Product Page:
http://www.vantorix.example/intl/en/halo/devices/buynow.html#instore

NOTE: I just added a file called "I like this color scheme.png" you can play around with something like this as well.
Updates

Please do not use the content from my current website. That is for a PPC service, the new site is for an full service agency.

Also, the message/tagline is the feature or most prominent element of the website..... Not the services we offer, these are secondary.

Great designs so far everyone, but I think I'm looking a little simpler and less crowded.  Closer to the sample sites I sent.... keep em coming.

Also, I would prefer that the 4 services, do not visually over power the tag line.  The 4 services are not important to the home page.

Lets make this easy, since every design I receive is almost the same...

Make the design look something like these 2 websites.
https://www.vantorix.example/intl/en/halo/browser/features.html#simplicity

Target Market(s)

Business Owners and entreprenuers who are well established, typically in the 35-60 year old range and spend 100k-1m in advertising per year. They big brands that target these people are Ravenmotor, Korel, Tamar, Brandin, Zepra, this should give you the feel for what I am after.

Industry/Entity Type

Advertising

Requirements
Must have
• 1. Navigations: Home, Services, About Us, Blog, Contact Us

2. The main home page words should be.... "We Grow Your Business Online" and "Clear Aim, Clear Plan, Clear Team, Bright Path Web Growth" (should use logo for last one)
I would like to see this tagline somewhere in the site "We Don't Want to be the Biggest, Just the Best!"

3. Product page must have a contact form with (name, email, phone, website)
This form must show an offer of "Free Strategy Sessions, Double your website leads", I have included an image to show as an example for the lead form "lead form example.png", see attached.

Nice to have
• I would like to see 1 or 2 of these idea's in the design.

1. I have attached some logos for Bidlane & Metricove certifications + Web association logo you can use for design purposes.

2. You can put company logo's in the design and I can change them to my clients logos at a later date.

3. Testimonials

4. Since our business is about people, pictures of people like business owners, customers using technology such as an slate, or anything like that would be good. However, is not necessary. Some idea: http://www.peerlattice.example/advertising
Should not have
• There will be no video on the design.

```html
<!DOCTYPE html>
<html lang="en">
<head>
<meta charset="utf-8">
<title>Bright Path Web Growth</title>
<link href="https://fonts.googleapis.com/css2?family=Arvo:wght@400;700&family=Open+Sans:wght@400;600;700&display=swap" rel="stylesheet">
<style>
:root{
  --blue-top:#4aa8dc;
  --blue-bottom:#2b86c4;
  --blue-link:#2a8fcf;
  --cyan:#1ab0e8;
  --green:#7fbf26;
  --green-dark:#5f9a12;
  --yellow:#f4e04a;
  --ink:#1f1f1f;
  --text:#4a4a4a;
  --muted:#8a8a8a;
  --hero-bg:#e7eef3;
  --hero-tile:#f4f8fb;
  --panel:#f2f5f8;
  --line:#dfe5ea;
  --footer:#1e1e1e;
  --footer-text:#9a9a9a;
  --white:#ffffff;
}
*{margin:0;padding:0;box-sizing:border-box}
html,body{width:689px;height:1200px;overflow:hidden}
body{position:relative;background:var(--panel);font-family:"Open Sans",Arial,sans-serif;color:var(--text)}
a{text-decoration:none;color:inherit}
.abs{position:absolute}

/* header */
.site-header{position:absolute;left:0;top:0;width:689px;height:68px;background:linear-gradient(var(--blue-top),var(--blue-bottom))}
.brand{position:absolute;left:91px;top:16px;display:flex;align-items:center;gap:7px;color:var(--white)}
.brand-mark{width:26px;height:26px;border-radius:50%;background:var(--white)}
.brand-name{font-weight:700;font-size:13px;line-height:13px;letter-spacing:-.2px}
.brand-name small{display:block;font-size:7px;font-weight:600;letter-spacing:1px;margin-top:2px}
.header-tagline{left:274px;top:19px;font-size:8px;color:#e4f3fc}
.phone-box{left:462px;top:14px;width:134px;height:20px;background:linear-gradient(#9ad03a,var(--green-dark));border-radius:2px;display:flex;align-items:center;color:var(--white);font-size:13px}
.phone-box .icon{width:22px;height:20px;display:flex;align-items:center;justify-content:center;border-right:1px solid rgba(0,0,0,.2);margin-right:8px}
.main-nav{right:88px;top:48px;display:flex;font-size:8.5px;color:var(--white)}
.main-nav span{margin:0 5px;color:#bfe0f4}
.main-nav .current{color:var(--yellow)}

/* hero */
.hero{position:absolute;left:0;top:68px;width:689px;height:248px;background:var(--hero-bg);overflow:hidden}
.tile{position:absolute;background:var(--hero-tile)}
.social{position:absolute;top:10px;display:flex;font-size:6.5px;color:#333}
.social .btn{border:1px solid #c7ccd1;background:var(--white);padding:1px 4px;border-radius:2px}
.social .count{border:1px solid #c7ccd1;background:var(--white);padding:1px 3px;margin-left:2px}
.portrait{position:absolute;left:131px;top:18px;width:163px;height:230px;background:linear-gradient(#d9c8bd,#3a3c47 60%,#262833);border-radius:60px 60px 0 0}
.script-note{position:absolute;left:36px;top:84px;width:100px;height:32px;background:rgba(120,120,120,.10);border-radius:3px}
.hero-title{position:absolute;left:356px;top:60px;font-family:"Arvo",Georgia,serif;font-weight:400;font-size:24px;line-height:25px;color:var(--ink)}
.hero-sub{position:absolute;left:357px;top:118px;font-size:10px;line-height:12px;color:#333}
.btn-review{position:absolute;display:flex;align-items:center;justify-content:center;flex-direction:column;background:linear-gradient(#3fa2dc,#1d6fb0);color:var(--white);border-radius:2px;box-shadow:0 1px 2px rgba(0,0,0,.2);text-decoration:none}
.btn-review b{font-family:"Arvo",Georgia,serif;font-weight:400;font-size:12px;line-height:13px}
.btn-review small{font-size:6.5px;line-height:8px;color:#cfe8f8}
.hero .btn-review{left:357px;top:150px;width:172px;height:33px;padding-left:40px;align-items:flex-start}
.hero .btn-review .glass{position:absolute;left:13px;top:10px}
.dots{position:absolute;left:303px;top:226px;display:flex;gap:8px}
.dots i{width:3px;height:3px;border-radius:50%;background:#555}
.dots i.on{width:6px;height:6px;margin-top:-1.5px;background:none;border:1px solid #555}

/* clients */
.clients{position:absolute;left:0;top:316px;width:689px;height:45px;background:var(--white);border-top:1px solid var(--line);border-bottom:1px solid var(--line)}
.clients-label{position:absolute;left:108px;top:-5px;background:var(--white);font-size:5.5px;letter-spacing:.6px;color:var(--muted);padding:0 4px}
.client{position:absolute;top:12px;display:flex;align-items:center;gap:4px;font-size:13px;color:#555}
.badge{width:32px;height:22px;background:#d6d9dc;border-radius:2px}
.client .dot{width:20px;height:20px;border-radius:50%;background:#777}

/* services */
.services{position:absolute;left:0;top:361px;width:689px;height:234px;background:#f7f8f9}
.service{position:absolute;top:28px;width:130px;text-align:center}
.service .pic{width:94px;height:94px;margin:0 auto;border-radius:50%;border:3px solid var(--white);box-shadow:0 1px 4px rgba(0,0,0,.18)}
.service h3{font-family:"Arvo",Georgia,serif;font-weight:400;font-size:9.5px;line-height:11px;color:var(--ink);margin-top:13px}
.service p{font-size:6.8px;line-height:9.5px;color:var(--muted);margin-top:5px;letter-spacing:-.1px}
.services .btn-review{left:251px;top:214px;width:187px;height:36px}

/* about */
.section-title{position:absolute;font-family:"Arvo",Georgia,serif;font-weight:400;font-size:16px;color:var(--ink)}
.about-text{position:absolute;left:88px;top:671px;width:520px;font-size:13.6px;line-height:18.5px;color:#333}
.highlight{background:var(--cyan);color:var(--white);font-weight:700;padding:0 4px}
.divider{position:absolute;left:88px;top:773px;width:510px;height:1px;background:var(--line)}

/* testimonials */
.testimonial{position:absolute;top:843px;width:150px}
.avatar{position:absolute;left:0;top:2px;width:26px;height:26px;background:#b9bcbf}
.person{margin-left:33px}
.person h4{font-weight:400;font-size:10px;line-height:11px;color:var(--blue-link)}
.person p{font-size:6.5px;line-height:9px;color:var(--muted);margin-top:3px}
.quote{font-size:8.2px;line-height:12px;color:#333;margin-top:7px;width:140px}
.quote-logo{margin-top:9px;font-size:10px;color:#666;display:flex;align-items:center;gap:4px}
.quote-logo i{width:9px;height:9px;background:#888;display:inline-block}

/* footer */
.site-footer{position:absolute;left:0;top:1026px;width:689px;height:174px;background:var(--footer)}
.footer-col{position:absolute;top:24px}
.footer-col h5{font-family:"Arvo",Georgia,serif;font-weight:400;font-size:10.5px;color:var(--white);margin-bottom:7px}
.footer-col li{list-style:none;font-size:7.5px;line-height:15px;color:var(--footer-text)}
.footer-col li::before{content:"›";color:var(--white);margin-right:4px;font-weight:700}
.footer-col p{font-size:7px;line-height:9.5px;color:var(--footer-text)}
.signup{display:flex;margin-top:7px}
.signup span{width:80px;height:15px;background:#f5f5f5;font-size:7px;color:#999;padding:3px 5px;white-space:nowrap;overflow:hidden}
.signup b{width:50px;height:15px;background:var(--green);color:var(--white);font-size:7px;text-align:center;line-height:15px;letter-spacing:.5px}
.map{position:absolute;left:389px;top:22px;width:102px;height:74px;background:linear-gradient(135deg,#e8e3d6,#d9d3c2);border:2px solid var(--white)}
.contact h5{font-family:"Open Sans",Arial,sans-serif;font-size:12px;margin-bottom:3px}
.contact .link{color:var(--green);font-size:7.5px;display:flex;align-items:center;gap:4px;line-height:12px}
.copyright{position:absolute;left:88px;top:137px;width:512px;border-top:1px solid #2e2e2e;padding-top:6px;text-align:center;font-size:7px;color:#777}
</style>
</head>
<body>

<header class="site-header">
  <div class="brand"><span class="brand-mark"></span><span class="brand-name">Bright Path<small>WEB GROWTH</small></span></div>
  <p class="abs header-tagline">We Don't Want to be the Biggest, Just the Best!</p>
  <div class="abs phone-box">
    <span class="icon"><svg width="10" height="10" viewBox="0 0 24 24"><path fill="#fff" d="M6.6 10.8a15.1 15.1 0 0 0 6.6 6.6l2.2-2.2c.3-.3.7-.4 1-.2 1.1.4 2.3.6 3.6.6.6 0 1 .4 1 1V20c0 .6-.4 1-1 1C10.6 21 3 13.4 3 4c0-.6.4-1 1-1h3.5c.6 0 1 .4 1 1 0 1.2.2 2.4.6 3.6.1.3 0 .7-.2 1z"/></svg></span>
    (020) 5550 1842
  </div>
  <nav class="abs main-nav">
    <a href="#">HOME</a><span>/</span><a href="#">SERVICES</a><span>/</span><a href="#">ABOUT US</a><span>/</span><a href="#">BLOG</a><span>/</span><a href="#" class="current">CONTACT US</a>
  </nav>
</header>

<section class="hero">
  <div class="tile" style="left:110px;top:60px;width:40px;height:40px"></div>
  <div class="tile" style="left:55px;top:143px;width:38px;height:38px"></div>
  <div class="tile" style="left:520px;top:28px;width:40px;height:40px"></div>
  <div class="tile" style="left:560px;top:68px;width:40px;height:40px"></div>
  <div class="tile" style="left:600px;top:28px;width:40px;height:40px"></div>
  <div class="tile" style="left:640px;top:68px;width:49px;height:40px"></div>
  <div class="tile" style="left:600px;top:108px;width:40px;height:40px"></div>
  <div class="tile" style="left:560px;top:148px;width:40px;height:40px"></div>
  <div class="tile" style="left:460px;top:188px;width:40px;height:60px"></div>
  <div class="tile" style="left:600px;top:188px;width:40px;height:60px"></div>
  <div class="tile" style="left:330px;top:160px;width:28px;height:40px"></div>
  <div class="social" style="left:482px"><span class="btn">Chirper</span><span class="count">112</span></div>
  <div class="social" style="left:539px"><span class="btn">Friendbook</span><span class="count">86</span></div>
  <div class="script-note" role="img" aria-label="Handwritten note: We Don't Want to be the Biggest, Just the Best!, with an arrow pointing to the portrait"></div>
  <div class="portrait" role="img" aria-label="Photo of a smiling businesswoman in a dark top"></div>
  <h1 class="hero-title">We Grow Your<br>Business Online</h1>
  <p class="hero-sub">Clear Aim, Clear Plan,<br>Clear Team, Bright Path Web Growth</p>
  <a class="btn-review" href="#">
    <svg class="glass" width="16" height="14" viewBox="0 0 16 14"><rect x=".5" y=".5" width="15" height="11" fill="none" stroke="#fff"/><circle cx="7" cy="6" r="2.6" fill="none" stroke="#fff" stroke-width="1.3"/><path d="M9 8l3 3" stroke="#fff" stroke-width="1.5"/></svg>
    <b>GET SEO REVIEW</b><small>It's free and always be</small>
  </a>
  <div class="dots"><i></i><i></i><i></i><i></i><i class="on"></i><i></i><i></i></div>
</section>

<section class="clients">
  <span class="clients-label">OUR CLIENTS ▾</span>
  <div class="client" style="left:88px;top:10px"><span class="badge" role="img" aria-label="Bidlane certification badge"></span></div>
  <div class="client" style="left:148px;font-size:7px;line-height:8px"><span class="dot"></span>Coastal Web<br>Guild</div>
  <div class="client" style="left:247px;top:10px"><span class="badge" role="img" aria-label="Metricove certification badge"></span></div>
  <div class="client" style="left:318px">Lumacorp</div>
  <div class="client" style="left:420px">Weddara.com</div>
  <div class="client" style="left:515px">Pokerline</div>
</section>

<section class="services">
  <div class="service" style="left:79px"><div class="pic" role="img" aria-label="Illustration of a tree made of business icons" style="background:radial-gradient(#fbe9e4,#f3b7ab)"></div><h3>Consulting &amp;<br>Strategy Planning</h3><p>In today's time, life without Searchly,<br>Quarry, Yodel! or any of their.</p></div>
  <div class="service" style="left:212px"><div class="pic" role="img" aria-label="Illustration of a search results page" style="background:radial-gradient(#f2faef,#b9e0ae)"></div><h3>Search Engine<br>Optimisation (SEO)</h3><p>In today's time, life without Searchly,<br>Quarry, Yodel! or any of their.</p></div>
  <div class="service" style="left:347px"><div class="pic" role="img" aria-label="Illustration of a hand clicking a green button" style="background:radial-gradient(#eef9fd,#a9dcf2)"></div><h3>Pay Per Click (PPC)</h3><p>In today's time, life without Searchly,<br>Quarry, Yodel! or any of their.</p></div>
  <div class="service" style="left:481px"><div class="pic" role="img" aria-label="Illustration of a person working at a laptop" style="background:radial-gradient(#f4f2fc,#cfc9ef)"></div><h3>Re-Marketing</h3><p>In today's time, life without Searchly,<br>Quarry, Yodel! or any of their.</p></div>
  <a class="btn-review" href="#"><b>GET SEO REVIEW</b><small>It's free and always be</small></a>
</section>

<h2 class="section-title" style="left:89px;top:647px">Who We Are</h2>
<p class="about-text">Bright Path Web Growth is not just another SEO or PPC company. We work with our clients to help them grow their business and achieve their <span class="highlight">goals.</span> Our commitment to doing what is best for the customer, is why we have grown so quickly.</p>
<div class="divider"></div>

<h2 class="section-title" style="left:89px;top:809px">What People Say</h2>
<article class="testimonial" style="left:89px">
  <div class="avatar" role="img" aria-label="Portrait photo of the reviewer"></div>
  <div class="person"><h4>Mateo<br>Alvarez</h4><p>Customer Experience and Social Media Manager at Vendora</p></div>
  <p class="quote">"We are delighted to work with the team RANKWISE our SEO strategy for their demonstrated professionalism and accomplishment. Notably adequacy SEO planning to the particularities of our markets."</p>
  <div class="quote-logo">Lumacorp</div>
</article>
<article class="testimonial" style="left:274px">
  <div class="avatar" role="img" aria-label="Portrait photo of the reviewer"></div>
  <div class="person"><h4>Mateo<br>Alvarez</h4><p>Director Pokerline</p></div>
  <p class="quote" style="margin-top:7px">"We are delighted to work with the team RANKWISE our SEO strategy for their demonstrated professionalism and accomplishment. Notably adequacy SEO planning to the particularities of our markets."</p>
  <div class="quote-logo">Weddara.com</div>
</article>
<article class="testimonial" style="left:455px">
  <div class="avatar" role="img" aria-label="Portrait photo of the reviewer"></div>
  <div class="person"><h4>Ravi<br>Deshmukh</h4><p>Customer Experience and Social Media Manager at Vendora</p></div>
  <p class="quote">"We are delighted to work with the team RANKWISE our SEO strategy for their demonstrated professionalism and accomplishment. Notably adequacy SEO planning to the particularities of our markets."</p>
  <div class="quote-logo">Vendora <i></i></div>
</article>

<footer class="site-footer">
  <div class="footer-col" style="left:88px">
    <h5>Our Services</h5>
    <ul><li>Consulting &amp; Strategy Planning</li><li>Search Engine Optimisation</li><li>Pay Per Click</li><li>Re-Marketing</li></ul>
  </div>
  <div class="footer-col" style="left:242px;width:130px">
    <h5>Stay Up to Date</h5>
    <p>Get the latest on Nodel, e-commerce, digital, design and social stuff straight to your inbox</p>
    <div class="signup"><span>user@mail.example</span><b>SIGNUP</b></div>
  </div>
  <div class="map" role="img" aria-label="Street map showing the office location"></div>
  <div class="footer-col contact" style="left:508px">
    <h5>(020) 5550 7394</h5>
    <p>48 Harbor Lane<br>Suite 310 New York<br>NY 10011</p>
    <div class="link" style="margin-top:5px"><svg width="7" height="6" viewBox="0 0 7 6"><rect width="7" height="6" fill="#ddd"/><path d="M0 0l3.5 3L7 0" stroke="#555" fill="none" stroke-width=".8"/></svg>Get In Touch</div>
    <div class="link"><svg width="6" height="8" viewBox="0 0 6 8"><path d="M3 8C1 5 0 4 0 3a3 3 0 0 1 6 0c0 1-1 2-3 5z" fill="#ddd"/></svg>Directions</div>
  </div>
  <p class="copyright">Copyright © 2012 Bright Path Web Growth®</p>
</footer>

</body>
</html>
```